Brindle Financial Advice - Employer Benefit Brochure

We need to design a professional looking brochure that we can present to our existing client base, and assist in attracting new clients.
The current information is just provided in a word document, but we need to improve significantly.
The audience would be business leaders, HR decision makers and member policy committee members

Industry/Entity Type

Business

Font styles to use
Sans Serif

Colors
0255a3
f37122

```html
<!DOCTYPE html>
<html lang="en">
<head>
<meta charset="utf-8">
<title>Brindle Financial Advice – Employer Benefits Program</title>
<link rel="stylesheet" href="https://fonts.googleapis.com/css2?family=Questrial&display=swap">
<style>
  :root {
    --brand-blue: #0255a3;
    --band-blue: #2e6fe0;
    --brand-orange: #f37122;
    --band-orange: #ff5a0a;
    --ink: #2a2a2a;
    --page: #ffffff;
    --backdrop: #e8e5e0;
    --table-head-top: #8fa3a0;
    --table-head-bottom: #5d7371;
    --table-stripe: #eef2f1;
    --table-rule: #c9d2d0;
    --badge: #3a3a3a;
  }
  * { margin: 0; padding: 0; box-sizing: border-box; }
  html, body { width: 1200px; height: 859px; overflow: hidden; }
  body {
    position: relative;
    background: var(--backdrop);
    font-family: "Questrial", "Century Gothic", sans-serif;
    color: var(--ink);
  }
  .spread {
    position: absolute; left: 38px; top: 32px;
    width: 1124px; height: 796px;
    background: var(--page);
    box-shadow: 0 2px 8px rgba(0,0,0,.15);
  }
  .spread-art { position: absolute; left: 0; top: 0; }
  .page-number {
    position: absolute; top: 743px;
    width: 30px; height: 30px; border-radius: 50%;
    background: var(--badge); color: #fff;
    font-size: 12px; line-height: 30px; text-align: center;
  }
  .page-number--left { left: 262px; }
  .page-number--right { left: 823px; }

  .content {
    position: absolute; left: 689px; top: 80px; width: 380px;
  }
  .title {
    font-weight: 400; font-size: 29.5px; line-height: 36px;
    color: var(--band-orange); white-space: nowrap;
  }
  .title .accent { color: var(--band-blue); }
  .subtitle {
    margin-top: 6px; font-weight: 400; font-size: 16.5px; line-height: 20px;
    color: var(--ink); white-space: nowrap;
  }
  .subtitle .label { color: var(--band-orange); margin-right: 6px; }
  .body-copy p {
    font-size: 13.4px; line-height: 15.6px; text-align: justify;
    letter-spacing: .05px;
  }
  .body-copy p:first-child { margin-top: 9px; }
  .body-copy .gap { margin-top: 10px; }
  .body-copy .gap-lg { margin-top: 18px; }

  .services {
    position: absolute; left: 686px; top: 496px; width: 387px;
    border-collapse: collapse;
    box-shadow: 0 3px 5px rgba(0,0,0,.25);
    background: #fff;
  }
  .services th {
    background: linear-gradient(var(--table-head-top), var(--table-head-bottom));
    color: #fff; font-weight: 400; font-size: 14px; height: 26px;
    border-right: 1px solid #fff;
  }
  .services th:last-child { border-right: 0; }
  .services td {
    font-size: 7.6px; line-height: 9.3px; vertical-align: top;
    padding: 4px 3px; border-top: 1px solid var(--table-rule);
  }
  .services tr:nth-child(even) td { background: var(--table-stripe); }
  .services .service-name {
    width: 93px; color: var(--band-orange);
    border-right: 1px solid var(--table-rule);
  }
  .services .service-detail { text-align: justify; }
</style>
</head>
<body>
<main class="spread">
  <svg class="spread-art" width="1124" height="796" viewBox="0 0 1124 796" aria-hidden="false">
    <defs>
      <linearGradient id="skyline" x1="0" y1="0" x2="0" y2="1">
        <stop offset="0" stop-color="#dfe8ee"/>
        <stop offset=".55" stop-color="#aebfcc"/>
        <stop offset="1" stop-color="#e9edf0"/>
      </linearGradient>
      <linearGradient id="sign" x1="0" y1="0" x2="1" y2="1">
        <stop offset="0" stop-color="#7fae5a"/>
        <stop offset=".5" stop-color="#2f6a3c"/>
        <stop offset="1" stop-color="#1f4d2d"/>
      </linearGradient>
      <linearGradient id="chalk" x1="0" y1="0" x2="1" y2="1">
        <stop offset="0" stop-color="#4b6fa0"/>
        <stop offset="1" stop-color="#1c3558"/>
      </linearGradient>
    </defs>
    <!-- diagonal bands -->
    <polygon class="band band--orange" points="452,0 672,0 525,218 262,218" fill="var(--band-orange)"/>
    <polygon class="band band--blue" points="0,713 333,218 525,218 137,796 0,796" fill="var(--band-blue)"/>
    <!-- photo areas -->
    <polygon role="img" aria-label="Photo of a businessman in a suit looking out over a city skyline"
      points="0,0 452,0 262,218 160,218 160,350 0,483" fill="url(#skyline)"/>
    <polygon role="img" aria-label="Photo of a green road sign reading Benefits"
      points="160,218 372,218 372,268 232,430 160,350" fill="url(#sign)"/>
    <polygon role="img" aria-label="Photo of a hand writing the word Benefit on a blue board"
      points="522,118 662,118 662,330 470,330 470,183" fill="url(#chalk)"/>
  </svg>

  <div class="page-number page-number--left">3</div>
  <div class="page-number page-number--right">4</div>

  <section class="content">
    <h1 class="title">Employer Benefits <span class="accent">Program</span></h1>
    <h2 class="subtitle"><span class="label">CORE:</span>Corporate Superannuation Services</h2>
    <div class="body-copy">
      <p>Brindle’s core offer is the ongoing support of the group employer superannuation solution.</p>
      <p class="gap">Superannuation is a long-term investment so it’s crucial to have the right partner who will consistently deliver outstanding support to you and your employees. Brindle has an extensive knowledge of superannuation providers in the market and can ensure that you have the right solution for your long-term business requirements.</p>
      <p>We are able to take over the servicing of the current group plan, or assist in setting up a plan for companies new to the market.</p>
      <p class="gap-lg">The program we deliver has two unique components. Firstly, services to assist employers in providing a ‘best of breed’ superannuation solution to employees and secondly, proactive advice to employees to ensure that they take control of their individual financial situation.</p>
      <p>Below is an overview of the services and support Brindle provides to employers:</p>
    </div>
  </section>

  <table class="services">
    <thead>
      <tr><th>Service</th><th>Brindle provides</th></tr>
    </thead>
    <tbody>
      <tr>
        <td class="service-name">Choosing your employer super plan</td>
        <td class="service-detail">Whether you are self-directed, or seeking a full advice service, we can assist you in your selection of the most suitable provider for your employees long-term retirement needs.</td>
      </tr>
      <tr>
        <td class="service-name">Setting up a new super plan</td>
        <td class="service-detail">We facilitate the complete application process, induction presentations for employees, lost super searches and the setting up of the online clearing facility for all your superannuation payments.</td>
      </tr>
      <tr>
        <td class="service-name">Managing and Reviewing your employer super plan</td>
        <td class="service-detail">We work together to build and deliver your annual Client Service Plan. We manage the annual review process, provide access to all relevant information and answer all employer and employee queries, complaints and facilitate the ongoing plan administration.</td>
      </tr>
      <tr>
        <td class="service-name">Policy Committee management</td>
        <td class="service-detail">We establish and manage a Policy Committee where required or desired. Responsibilities include initiating all meetings, preparing reports, minutes and the presentation of legislative product and education updates.</td>
      </tr>
      <tr>
        <td class="service-name">Keeping you up to date</td>
        <td class="service-detail">We provide you with all relevant communications to ensure that you meet your responsibilities and obligations.</td>
      </tr>
    </tbody>
  </table>
</main>
</body>
</html>
```